Pale Harbor car

Vornex model Q in silver partial wrap not full wrap to look cool for my company called :
Pale Harbor Designed Construction
also there’s a slogan but not urgent
“Insurance Jobs Welcome”

```html
<!DOCTYPE html>
<html lang="en">
<head>
<meta charset="utf-8">
<title>Pale Harbor – Vornex model Q partial wrap</title>
<link rel="stylesheet" href="https://fonts.googleapis.com/css2?family=Oswald:wght@500;600;700&family=Yellowtail&family=Montserrat:wght@500&display=swap">
<style>
  :root {
    --bg: #eef0f2;
    --silver-light: #d3d6da;
    --silver-dark: #9ca1a7;
    --wrap-blue: #1f4a94;
    --wrap-blue-deep: #163a7a;
    --ring-blue: #1c3f82;
    --white: #ffffff;
    --photo-sky: #b9c4cf;
    --photo-wall: #8e8f93;
    --photo-pool: #3aa6c4;
    --photo-green: #5d7f3c;
    --photo-interior: #d9d2c6;
  }
  html, body {
    margin: 0;
    padding: 0;
    width: 1170px;
    height: 1200px;
    overflow: hidden;
    background: var(--bg);
  }
  .wrap-canvas { display: block; width: 1170px; height: 1200px; }
  .slogan { font-family: "Yellowtail", cursive; fill: var(--white); }
  .brand-name { font-family: "Oswald", sans-serif; font-weight: 700; fill: var(--white); }
  .established { font-family: "Oswald", sans-serif; font-weight: 600; fill: var(--white); }
  .tagline { font-family: "Montserrat", sans-serif; font-weight: 500; fill: var(--white); letter-spacing: 7px; }
  .service-label { font-family: "Oswald", sans-serif; font-weight: 500; fill: var(--white); }
  .website { font-family: "Oswald", sans-serif; font-weight: 700; fill: var(--ring-blue); stroke: var(--white); stroke-width: 2; paint-order: stroke; }
  .phone { font-family: "Oswald", sans-serif; font-weight: 600; fill: var(--white); }
</style>
</head>
<body>
<svg class="wrap-canvas" viewBox="0 0 1170 1200" xmlns="http://www.w3.org/2000/svg">
  <defs>
    <linearGradient id="silverBody" x1="0" y1="0" x2="0" y2="1">
      <stop offset="0" stop-color="var(--silver-light)"/>
      <stop offset="1" stop-color="var(--silver-dark)"/>
    </linearGradient>
    <linearGradient id="blueBody" x1="0" y1="0" x2="1" y2="1">
      <stop offset="0" stop-color="var(--wrap-blue)"/>
      <stop offset="1" stop-color="var(--wrap-blue-deep)"/>
    </linearGradient>
    <linearGradient id="houseBackdrop" x1="0" y1="0" x2="0" y2="1">
      <stop offset="0" stop-color="var(--photo-sky)"/>
      <stop offset="1" stop-color="var(--photo-wall)"/>
    </linearGradient>
    <linearGradient id="poolPhoto" x1="0" y1="0" x2="0" y2="1">
      <stop offset="0" stop-color="#e7b27c"/>
      <stop offset="0.55" stop-color="#5e6b55"/>
      <stop offset="1" stop-color="var(--photo-pool)"/>
    </linearGradient>
    <linearGradient id="interiorPhoto" x1="0" y1="0" x2="0" y2="1">
      <stop offset="0" stop-color="#f3efe8"/>
      <stop offset="1" stop-color="var(--photo-interior)"/>
    </linearGradient>
    <linearGradient id="gardenPhoto" x1="0" y1="0" x2="0" y2="1">
      <stop offset="0" stop-color="#e8c79a"/>
      <stop offset="0.5" stop-color="var(--photo-green)"/>
      <stop offset="1" stop-color="#b8b6ae"/>
    </linearGradient>
  </defs>

  <rect class="silver-panel" x="0" y="200" width="1170" height="800" fill="url(#silverBody)"/>

  <polygon class="house-backdrop" role="img" aria-label="Photo of a Spanish-style house exterior at dusk"
           points="620,200 1030,200 900,1000 500,1000" fill="url(#houseBackdrop)" opacity="0.9"/>

  <path class="blue-panel" d="M120,200 L700,200 C660,420 600,700 560,1000 L0,1000 L0,820 Z" fill="url(#blueBody)"/>

  <g class="service-circle">
    <circle cx="740" cy="400" r="88" fill="var(--ring-blue)"/>
    <circle cx="740" cy="400" r="83" fill="var(--white)"/>
    <circle cx="740" cy="400" r="78" fill="url(#poolPhoto)" role="img" aria-label="Photo of a backyard with pool at sunset"/>
  </g>
  <g class="service-circle">
    <circle cx="690" cy="600" r="88" fill="var(--ring-blue)"/>
    <circle cx="690" cy="600" r="83" fill="var(--white)"/>
    <circle cx="690" cy="600" r="78" fill="url(#interiorPhoto)" role="img" aria-label="Photo of a bright living room interior"/>
  </g>
  <g class="service-circle">
    <circle cx="640" cy="800" r="88" fill="var(--ring-blue)"/>
    <circle cx="640" cy="800" r="83" fill="var(--white)"/>
    <circle cx="640" cy="800" r="78" fill="url(#gardenPhoto)" role="img" aria-label="Photo of a single-storey home with garden"/>
  </g>

  <text class="service-label" x="845" y="410" font-size="26">DESIGN &amp; ENGINEERING</text>
  <text class="service-label" x="795" y="610" font-size="26">ENTITLEMENTS &amp; PERMITTING</text>
  <text class="service-label" x="745" y="798" font-size="26">PERMIT EXPEDITING &amp;</text>
  <text class="service-label" x="745" y="830" font-size="26">PROCUREMENT</text>

  <text class="website" x="1150" y="255" font-size="40" text-anchor="end">WWW.PALEHARBORBUILD.COM</text>
  <text class="phone" x="1150" y="320" font-size="54" text-anchor="end">000.000.000</text>

  <text class="slogan" x="310" y="410" font-size="52" text-anchor="middle">Insurance Jobs Welcome</text>
  <text class="brand-name" x="310" y="540" font-size="100" text-anchor="middle">PALE HARBOR</text>
  <g class="established-line">
    <line x1="150" y1="596" x2="220" y2="596" stroke="var(--white)" stroke-width="4" stroke-linecap="round"/>
    <text class="established" x="310" y="612" font-size="42" text-anchor="middle">EST. 1996</text>
    <line x1="400" y1="596" x2="470" y2="596" stroke="var(--white)" stroke-width="4" stroke-linecap="round"/>
  </g>
  <text class="tagline" x="310" y="740" font-size="24" text-anchor="middle">PLAN · DESIGN · BUILD</text>
</svg>
</body>
</html>
```